Website design needed for Renewable utilities company based in New Zealand.

Website design needed for Tarnwick Collective based in New Zealand.

Please see attached logo.

We sell solar panels, vertical axis wind turbines, atmospheric water generators and other related equipment for those who don't have access or don't want to depend on the government, city councils for their utilities (power and water).

We like metallic texture, dark grey and purple, red or blue colours. The design should go well with the attached logo.

Target Market(s)

The Eco conscious

Industry/Entity Type

Government

Logo Text

Tarnwick Horizon

Requirements
Must have
• Must Have:
- Metallic finish is a must.
- Design should fit around the attached logo well.
Nice to have
• Sharpe design prefred rather than rounded edges

```html
<!DOCTYPE html>
<html lang="en">
<head>
<meta charset="utf-8">
<title>Tarnwick Horizon — Off-Grid Power &amp; Water</title>
<link rel="stylesheet" href="https://fonts.googleapis.com/css2?family=Alegreya+Sans:wght@400;500;700&display=swap">
<style>
  :root {
    --steel-light: #e4e6ea;
    --steel-mid: #b7bbc3;
    --steel-dark: #8e939c;
    --ink: #14161b;
    --slate-text: #5d6270;
    --brand-blue: #1a4fa0;
    --navy: #0b1a5e;
    --white: #ffffff;
    --charcoal: #222222;
    --muted-grey: #8c8c8c;
    --sky-deep: #26478f;
    --sky-light: #3d62b0;
    --social-tile: #4a5d8f;
  }
  * { box-sizing: border-box; margin: 0; padding: 0; }
  html, body { width: 1200px; height: 900px; overflow: hidden; }
  body {
    position: relative;
    font-family: "Alegreya Sans", "Helvetica Neue", Arial, sans-serif;
    background: var(--white);
    color: var(--ink);
  }

  /* Hero */
  .hero {
    position: absolute; left: 0; top: 0; width: 1200px; height: 515px;
    background:
      repeating-linear-gradient(180deg, rgba(255,255,255,0.10) 0 1px, rgba(0,0,0,0.04) 1px 3px, rgba(255,255,255,0) 3px 5px),
      radial-gradient(ellipse 55% 60% at 55% 45%, var(--steel-light) 0%, rgba(228,230,234,0) 70%),
      linear-gradient(90deg, var(--steel-dark) 0%, var(--steel-mid) 25%, var(--steel-light) 55%, var(--steel-mid) 80%, var(--steel-dark) 100%);
  }
  .brand {
    position: absolute; left: 34px; top: 14px; width: 142px;
    display: flex; flex-direction: column; align-items: center;
  }
  .brand-mark {
    width: 62px; height: 62px; border-radius: 50%;
    background: var(--brand-blue);
  }
  .brand-name {
    margin-top: 6px; font-size: 19px; font-weight: 500;
    color: var(--brand-blue); white-space: nowrap;
  }
  .top-info {
    position: absolute; left: 465px; top: 19px; width: 275px;
    color: var(--white); text-transform: uppercase;
  }
  .top-info .tagline { font-size: 10px; line-height: 13px; }
  .top-info .phone {
    display: flex; align-items: center; justify-content: center; gap: 7px;
    margin-top: 7px; font-size: 16px; letter-spacing: 0.5px; padding-right: 20px;
  }
  .menu-toggle {
    position: absolute; left: 1069px; top: 20px;
    display: flex; align-items: center; gap: 14px;
    color: var(--white); font-size: 15px; letter-spacing: 0.5px;
  }
  .menu-toggle .bars { display: flex; flex-direction: column; gap: 4px; }
  .menu-toggle .bars span { display: block; width: 35px; height: 4px; background: var(--white); }

  .hero-copy { position: absolute; left: 226px; top: 197px; width: 275px; }
  .hero-copy h1 { font-size: 28px; font-weight: 400; line-height: 32px; color: var(--ink); }
  .hero-copy .lead {
    font-size: 14px; line-height: 18px; color: var(--slate-text);
    text-transform: uppercase; text-align: justify; letter-spacing: 0.3px;
  }
  .hero-copy .body {
    margin-top: 3px; font-size: 10px; line-height: 13.7px; color: var(--white);
    text-transform: uppercase;
  }
  .cta {
    position: absolute; left: 226px; top: 400px; width: 141px; height: 36px;
    background: var(--navy); color: var(--white);
    font-size: 14px; display: flex; align-items: center; justify-content: center;
    text-transform: uppercase;
  }
  .scroll-cue { position: absolute; left: 280px; top: 469px; }
  .hero-visual {
    position: absolute; left: 530px; top: 125px; width: 355px; height: 370px;
    background: linear-gradient(180deg, rgba(160,165,172,0.15) 0%, rgba(120,125,134,0.55) 60%, rgba(70,74,82,0.7) 100%);
  }

  /* Navigation */
  .site-nav {
    position: absolute; left: 0; top: 515px; width: 1200px; height: 89px;
    background: var(--white);
  }
  .site-nav ul {
    list-style: none; position: absolute; left: 309px; top: 23px;
    display: flex; gap: 26px; font-size: 14px; text-transform: uppercase;
  }
  .site-nav li.active { font-weight: 700; position: relative; }
  .site-nav li.active::before {
    content: ""; position: absolute; left: 36px; top: -23px;
    border-left: 10px solid transparent; border-right: 10px solid transparent;
    border-top: 12px solid var(--ink);
  }
  .social-panel {
    position: absolute; left: 1080px; top: 490px; width: 84px; height: 104px;
    background: var(--white); border: 1px solid #dfe1e6;
    display: grid; grid-template-columns: repeat(3, 20px); gap: 5px;
    padding: 5px; justify-content: center; align-content: center;
  }
  .social-panel span { width: 20px; height: 20px; background: var(--social-tile); }

  /* Statement */
  .statement {
    position: absolute; left: 0; top: 604px; width: 1200px; height: 224px;
    background: var(--charcoal);
  }
  .statement p {
    position: absolute; left: 285px; top: 66px; width: 680px;
    font-size: 22px; line-height: 29px; color: var(--muted-grey);
    text-transform: uppercase;
  }

  /* Next band */
  .feature-band {
    position: absolute; left: 0; top: 828px; width: 1200px; height: 72px;
    background: linear-gradient(90deg, var(--sky-deep) 0%, var(--sky-light) 55%, var(--sky-deep) 100%);
  }
</style>
</head>
<body>
  <header class="hero">
    <div class="brand">
      <div class="brand-mark"></div>
      <div class="brand-name">Tarnwick Horizon</div>
    </div>

    <div class="top-info">
      <p class="tagline">Lorem ipsum dolor sit amet, consectetur adipiscing elit. Vestibulum fermentum erat urna, ut sagittis</p>
      <p class="phone">
        <svg width="13" height="13" viewBox="0 0 24 24" aria-hidden="true"><path fill="#fff" d="M6.6 10.8a15.1 15.1 0 0 0 6.6 6.6l2.2-2.2c.3-.3.7-.4 1-.2 1.1.4 2.3.6 3.6.6.6 0 1 .4 1 1V20c0 .6-.4 1-1 1A17 17 0 0 1 3 4c0-.6.4-1 1-1h3.5c.6 0 1 .4 1 1 0 1.3.2 2.5.6 3.6.1.3 0 .7-.2 1z"/></svg>
        0800 555 0199
      </p>
    </div>

    <div class="menu-toggle">MENU <span class="bars"><span></span><span></span><span></span></span></div>

    <div class="hero-copy">
      <h1>LOREM IPSUM</h1>
      <p class="lead">Lorem ipsum dolor sit amet, consecte adipiscing elit. Vestibulum fermentum erat urna</p>
      <p class="body">Lorem ipsum dolor sit amet, consectetur adipiscing elit. Vestibulum fermentum erat urna, ut sagittis orci dapibus ut. Curabitur a hendrerit diam, et commodo tortor. Fusce quam quam, vehicula ac consectetur vestibulum, interdum eget enim. Aenean eu lorem sed ante fringilla blandit facilisis at nisl.</p>
    </div>
    <a class="cta">Get started</a>
    <svg class="scroll-cue" width="30" height="20" viewBox="0 0 30 20" aria-hidden="true"><polyline points="1,1 15,18 29,1" fill="none" stroke="#fff" stroke-width="2"/></svg>

    <div class="hero-visual" role="img" aria-label="Illustration of a modern house with rooftop solar panels, a tree and a wind turbine"></div>
  </header>

  <nav class="site-nav">
    <ul>
      <li>Lorem ipsum</li>
      <li>Lorem ipsum</li>
      <li class="active">Lorem ipsum</li>
      <li>Lorem ipsum</li>
      <li>Lorem ipsum</li>
    </ul>
  </nav>

  <div class="social-panel" aria-label="Social links">
    <span></span><span></span><span></span>
    <span></span><span></span><span></span>
    <span></span><span></span><span></span>
    <span></span><span></span><span></span>
  </div>

  <section class="statement">
    <p>Lorem ipsum dolor sit amet, consectetur adipiscing elit. Curabitur ac dolor tincidunt, faucibus orci ut, egestas erat. Suspendisse congue felis sit amet est dictum mattis.</p>
  </section>

  <section class="feature-band" role="img" aria-label="Photograph of a wind turbine tower against a deep blue sky"></section>
</body>
</html>
```